new gp medical practice needs design for a flyer for a letter-box drop

need design for a flyer for a new general medical practice called "Brellmoor General Practice" in Tamworth NSW.
practice provides a full GP medical service to individuals and families.
general feel as in uploaded images, but will look at totally new ideas.
final design to communicate care, professionalism, access, availability, family friendly (i.e. all age groups catered for - from babies thru to old age), commitment.
must have call to immediate action for potential customers/ patients, so they think in their heads 'I must go see the doctor now' in addition to just 'oh yes good. I should remember these guys when I get sick'
all residents of a large rural town and surrounding villages and/ farms. Tamworth is the Australian capital of country music, similar to Nashville in the U.S.
Medical

```html
<!DOCTYPE html>
<html lang="en">
<head>
<meta charset="utf-8">
<title>Brellmoor General Practice – Flyer</title>
<link href="https://fonts.googleapis.com/css2?family=Didact+Gothic&family=Mulish:wght@700;800&family=Arimo:ital,wght@1,400;1,700&family=Open+Sans:wght@600&family=Roboto+Condensed:wght@500&display=swap" rel="stylesheet">
<style>
  :root {
    --sky: #cde5f2;
    --sky-pale: #dcebf6;
    --meadow: #d7dc8c;
    --panel: rgba(226, 238, 246, 0.55);
    --green: #33ad4a;
    --ink: #111111;
    --white: #ffffff;
  }
  * { box-sizing: border-box; margin: 0; padding: 0; }
  html, body { width: 1131px; height: 1200px; overflow: hidden; }
  body { font-family: "Didact Gothic", sans-serif; color: var(--ink); }

  .flyer {
    position: relative;
    width: 1131px;
    height: 1200px;
    overflow: hidden;
    background: linear-gradient(to bottom, var(--sky) 0, var(--sky) 686px, var(--meadow) 690px, var(--meadow) 100%);
  }

  /* brand */
  .brand-cloud { position: absolute; left: 18px; top: 8px; width: 520px; height: 270px; }
  .brand-name {
    position: absolute; left: 60px; top: 84px; width: 420px;
    font-family: "Didact Gothic", sans-serif; font-weight: 400; color: var(--ink);
    font-size: 44px; line-height: 54px; text-align: center;
  }

  /* call to action */
  .cta-box {
    position: absolute; left: 0; top: 298px; width: 566px; height: 163px;
    background: var(--sky-pale);
    display: flex; align-items: center; justify-content: center; text-align: center;
  }
  .cta-box h1 { font-family: "Didact Gothic", sans-serif; font-weight: 400; font-size: 47px; line-height: 54px; letter-spacing: 0.3px; }

  .family-art {
    position: absolute; left: 10px; top: 513px; width: 551px; height: 222px;
    border-radius: 18px;
    background: linear-gradient(to bottom, #f2c9a8 0%, #e6a07a 45%, #c98f6a 100%);
    opacity: 0.85;
  }

  /* well check */
  .well-check { position: absolute; left: 40px; top: 780px; width: 510px; }
  .well-check h2 {
    font-family: "Arimo", sans-serif; font-style: italic; font-weight: 700;
    font-size: 29.5px; line-height: 34px; text-align: center;
  }
  .well-check p { margin-top: 20px; padding-left: 14px; font-size: 23.5px; line-height: 29.5px; letter-spacing: 0.8px; white-space: nowrap; }

  /* services */
  .services {
    position: absolute; left: 612px; top: 24px; width: 475px; height: 997px;
    background: var(--panel); padding: 6px 0 0 20px;
    font-size: 23.5px; line-height: 26.6px; letter-spacing: 0.9px; white-space: nowrap;
  }
  .service-group { margin-bottom: 26.6px; }
  .service-group h3 { font-family: "Mulish", sans-serif; font-weight: 700; font-size: 22.5px; letter-spacing: 0.2px; }
  .service-group ul { list-style: none; }
  .service-bullets li::before { content: "•"; }
  .conditions { padding-left: 70px; }
  .conditions li::before { content: "◦"; }
  .indent { padding-left: 12px; }

  /* footer tabs */
  .tab {
    position: absolute; background: var(--white);
    border: 6px solid var(--green); border-bottom: none;
    border-radius: 34px 34px 0 0;
  }
  .tab-left { left: 24px; top: 1055px; width: 518px; height: 60px; display: flex; align-items: center; justify-content: center; }
  .tab-left span { font-family: "Arimo", sans-serif; font-style: italic; font-weight: 400; font-size: 30px; }
  .tab-right {
    left: 590px; top: 1038px; width: 518px; height: 77px;
    font-family: "Roboto Condensed", sans-serif; font-weight: 500; font-size: 20.7px;
    text-align: center; line-height: 30px; padding-top: 2px; white-space: nowrap;
  }

  .footer-bar {
    position: absolute; left: 0; top: 1113px; width: 1131px; height: 87px;
    background: var(--green); color: var(--white);
    font-family: "Open Sans", sans-serif; font-weight: 600; font-size: 26px; line-height: 38px;
    display: flex;
  }
  .footer-bar div { text-align: center; padding-top: 5px; }
  .footer-bar .contact { width: 566px; }
  .footer-bar .hours { width: 565px; }
</style>
</head>
<body>
<main class="flyer">
  <svg class="brand-cloud" viewBox="0 0 520 270" aria-hidden="true">
    <path d="M60 200 C10 190 10 120 60 110 C60 50 140 30 180 60 C220 10 330 0 370 50 C440 40 520 90 490 150 C520 200 460 250 400 225 C360 260 290 265 250 240 C200 265 120 250 110 220 C90 225 70 215 60 200 Z" fill="#ffffff" opacity="0.9"/>
  </svg>
  <div class="brand-name">Brellmoor<br>General Practice</div>

  <section class="cta-box">
    <h1>Drop in NOW for a full<br>medical GP Service!</h1>
  </section>

  <div class="family-art" role="img" aria-label="Cartoon illustration of a smiling family of six holding hands: grandparents, two young children and parents"></div>

  <section class="well-check">
    <h2>Have you had your annual well<br>check?</h2>
    <p>Our practice considers prevention of<br>illness, and maintaining excellent health<br>is really important. We encourage all<br>adults to have a well woman or well<br>man’s check every one to two years</p>
  </section>

  <aside class="services">
    <div class="service-group">
      <h3>Well Women’s check ups include:</h3>
      <ul>
        <li>Pap smears</li><li>Breast checks</li><li>Contraception</li><li>Sexual health checks</li>
        <li>Shared pregnancy care</li><li>Postnatal care</li><li>Skin check</li>
      </ul>
    </div>
    <div class="service-group">
      <h3>Men’s health check ups include:</h3>
      <ul>
        <li>Heart and lung checks</li><li>Prostate/testicular checks</li><li>Sexual health checks</li><li>Skin check</li>
      </ul>
    </div>
    <div class="service-group">
      <h3>Children’s health includes:</h3>
      <ul>
        <li>Baby checks</li><li>Developmental checks</li><li>Free childhood immunisations</li>
      </ul>
    </div>
    <div class="service-group">
      <h3>As well as...</h3>
      <ul class="service-bullets">
        <li>Minor surgery</li>
        <li>Travel health advice and vaccinations</li>
        <li>Weight loss management</li>
        <li>Quitting smoking advice</li>
        <li>Stress management</li>
        <li>Dive medicals</li>
        <li>Insurance medicals</li>
        <li>Work place injuries</li>
        <li>GP management of long term medical<br><span class="indent">conditions, such as:</span></li>
      </ul>
      <ul class="conditions">
        <li>Asthma</li><li>Diabetes</li><li>High blood pressure</li><li>High cholesterol</li>
        <li>Osteoarthritis</li><li>Chronic airways disease</li>
      </ul>
    </div>
  </aside>

  <div class="tab tab-left"><span>Healthcare for the whole family</span></div>
  <div class="tab tab-right">
    Permanent Full-Time GP | New Patients Welcome<br>
    Walk-Ins Welcome | Nursing Home Visits | House Calls
  </div>

  <footer class="footer-bar">
    <div class="contact">148 Corlen Street (next to the post office)<br>6700 4120</div>
    <div class="hours">Open 9-5 Weekdays with afterhours<br>Pre-Booked Saturday appointments</div>
  </footer>
</main>
</body>
</html>
```